Modern Ebook Design: The Lookout's Handbook for Outreach: Small Business Outreach Tips from the DKR

I need to convert a document I've written into an ebook for my marketing company, Tallgrove Advisory. The ebook, as mentioned, is about lessons I learned as a DKR officer that can be used for small business marketing. The title I'm thinking of right now "The Lookout's Handbook for Outreach: Tricks for Small Business Outreach from the DKR" (but I'm open to other suggestions). The design should, obviously, make playful use of the DKR theme but the key is PLAYFUL. It needs to be fun, engaging, exciting and very modern. Graphics and other design elements are good, so if there's something you think something could use a graphic to accompany the page, go for it. This will be serve as a downloadable ebook on my website, so I'd like there to be a place for a bio on the back and a hyperlinked call-to-action button for people to schedule a free marketing strategy session with my company (the link is avs.tallgroveadvisory.com/free-marketing-strategy-session). I need to have a final version done by 2/11 since I have a hard deadline to post it by 2/12.

The targets are owners of small businesses with revenue between $300,000 and $5 million.

Small Business

Sans Serif

• It must be modern, engaging, and visual interesting. It also needs to easy to read so be careful with your font selection too. I'm a big fan of Helvetica Neue Light and similar style fonts (doesn't have to be Helvetica family but prefer some sans-serif). A poor selection of fonts is going to color my view of the entire design, so be careful. Red, black, and grey play into my logo and branding a lot now so variations of those are good. I use red hex #99000 for all red images on my website and in my marketing (see tallgroveadvisory.com). There should also be some graphics to illustrate the points made in the text. They need to feel like organic parts of the book, not just slapped in there. Check out some examples at http://www.wexlamp.com/free-marketing-resources. Finally, please put hyperlinked social sharing icons for Friendlane, Chirply, Workweave, Q+.
• I'm wary of cartoonish images, but might be persuaded if they looked right. Small font isn't good either.

```html
<!DOCTYPE html>
<html lang="en">
<head>
<meta charset="utf-8">
<title>The Lookout's Handbook for Outreach — Spread</title>
<link href="https://fonts.googleapis.com/css2?family=Roboto:wght@300;400;700;900&display=swap" rel="stylesheet">
<style>
  :root{
    --red:#990000;
    --ink:#1f1f1f;
    --text:#3a3a3a;
    --paper:#f2f2f2;
    --page-grey:#d9d9d9;
    --title-grey:#a8a8a8;
    --dark-grey:#8c8c8c;
    --white:#ffffff;
  }
  *{box-sizing:border-box;margin:0;padding:0}
  html,body{width:1200px;height:388px;overflow:hidden;background:var(--white)}
  body{font-family:"Roboto",Helvetica,Arial,sans-serif;color:var(--text)}
  .spread{position:relative;width:1200px;height:388px;overflow:hidden}
  .page{position:absolute;top:0;width:300px;height:388px;overflow:hidden}
  .page--cover{left:0;background:var(--paper)}
  .page--inside-a{left:300px;background:var(--page-grey)}
  .page--inside-b{left:600px;background:var(--page-grey)}
  .page--back{left:900px;background:linear-gradient(180deg,#8f8f8f 0%,#b9b9b9 55%,#d8d8d8 100%)}
  .page--inside-a{border-left:1px solid #c4c4c4}
  .page--inside-b{border-left:1px solid #c4c4c4}

  .band{position:absolute;left:0;top:196px;width:1200px;height:64px;background:var(--red)}

  /* brand */
  .brand{position:absolute;text-align:center;color:var(--ink);font-weight:900;text-transform:uppercase;line-height:1}
  .brand--top{left:95px;top:8px;width:110px;font-size:9px;letter-spacing:1.5px}
  .brand--top .presents{display:block;margin-top:4px;font-size:7px;font-weight:400;text-transform:none;letter-spacing:0}
  .brand--bottom{left:1035px;top:348px;width:110px;font-size:8px;letter-spacing:1.5px}
  .brand .dot{display:inline-block;width:6px;height:6px;background:var(--red);margin-right:4px;vertical-align:middle}

  .cover-title{position:absolute;left:12px;top:68px;width:285px;font-weight:300;font-size:22px;line-height:26px;color:var(--title-grey)}
  .cover-title strong{font-weight:700;color:#8a8a8a}

  .cover-photo{position:absolute;left:0;top:260px;width:300px;height:128px;background:linear-gradient(135deg,#ffffff 0%,#e0e0e0 45%,#9d9d9d 100%)}
  .cover-quote{position:absolute;left:8px;top:286px;width:168px;font-size:8px;line-height:9.6px;font-weight:700;color:var(--ink)}

  /* body copy */
  .copy{position:absolute;font-size:5.6px;line-height:6.8px;color:var(--text);overflow:hidden}
  .copy p{margin-bottom:1px}
  .copy h3{font-size:6.6px;line-height:8px;font-weight:700;color:var(--ink);margin:3px 0 1px}
  .copy h3 .num{display:inline-block;width:8px;height:8px;border-radius:50%;background:var(--red);color:var(--white);font-size:5.5px;line-height:8px;text-align:center;margin-right:5px;vertical-align:top}
  .copy--on-red{color:var(--white)}
  .copy--on-red h3{color:var(--white)}
  .copy--on-red h3 .num{background:var(--white);color:var(--red)}

  .bio-heading{position:absolute;left:912px;top:8px;font-weight:300;font-size:18px;color:var(--white)}

  .lens-photo{position:absolute;left:1040px;top:150px;width:160px;height:170px;background:radial-gradient(circle at 45% 45%,#e6e6e6 0%,#bcbcbc 45%,#7a7a7a 70%,rgba(120,120,120,0) 72%)}
  .cta{position:absolute;left:1062px;top:192px;width:112px;height:112px;border-radius:50%;display:flex;align-items:center;justify-content:center;text-align:center;font-weight:700;font-size:12px;line-height:15px;color:var(--white);text-decoration:none;background:rgba(120,120,120,0.55);border:4px solid #444}
</style>
</head>
<body>
<main class="spread">

  <section class="page page--cover">
    <div class="brand brand--top"><span class="dot"></span>Tallgrove Advisory<span class="presents">presents:</span></div>
    <h1 class="cover-title">The Lookout's Handbook for <strong>Outreach:</strong> Tricks for Small Business Outreach from the <strong>DKR</strong></h1>
    <div class="cover-photo" role="img" aria-label="Soft greyscale photo of a magnifying glass"></div>
    <p class="cover-quote">What a lot of people don't realize is that marketing for small businesses and intelligence work are two sides of the same coin. They're both really about trying to understand another person's motivation and then figuring out how to influence them to take a specific action.</p>
  </section>

  <section class="page page--inside-a"></section>
  <section class="page page--inside-b"></section>
  <section class="page page--back">
    <h2 class="bio-heading">Biography:</h2>
  </section>

  <div class="band"></div>

  <!-- Inside page A -->
  <div class="copy" style="left:310px;top:4px;width:282px;height:192px">
    <h3><span class="num">1</span>Hope Isn't an Operational Plan…</h3>
    <p>One of the first things junior DKR officers learn is that, even in the fastest moving operations, you simply can't cross your fingers and assume it's all going to work out. We were reminded of this after the 2010 Varnost disaster, where a suicide bombing by a supposed asset killed 7 DKR and foreign officers and wounded several more. We were so wrapped up in the details and swept away by the speed of events that we never really took a step back to evaluate what was happening. This very personally painful example drove home to me that there's never not enough time to think strategically. In fact, it's usually when you don't think you have time, that planning is most important.</p>
    <p>You aren't going to face such and life and death situation. The usual example we see is a business feeling so much pressure to start selling more now that they start throwing money at all kinds of things—new website, ads, fancy signs—and just hoping it somehow works. But, if we learned that we had to pause and think strategically even in the most extreme situations, you can certainly do it for your business.</p>
    <h3><span class="num">2</span>…But No Plan Survives First Contact with the Enemy</h3>
    <p>I worked in an office that operated around the clock in three shifts. My team's job was to draft the operational plan for the next 24 hours to keep all three shifts working towards the same end. We'd usually give 3-4 operational priorities with as many as 10 tactical objectives to achieve under each. The problem was that events kept evolving, so our priorities and specific tasks had to change too. We joked that the plan was usually out-of-date the moment we hit "send." As frustrating as that was, we were spectacularly successful because we learned to be extremely tactically flexible in pursuit of an unchanging strategic goal.</p>
  </div>
  <div class="copy copy--on-red" style="left:310px;top:198px;width:282px;height:60px">
    <p>This same approach is one of the hallmarks of excellent marketing. No one—not even a marketing consultant—can predict exactly how any specific tactic is going to work ahead of time. If you have planned properly, you should be confident enough in your strategic goals to quickly tweak or junk any specific tactic when it becomes clear it isn't working.</p>
  </div>
  <div class="copy" style="left:310px;top:262px;width:282px;height:124px">
    <h3><span class="num">3</span>Building Rapport with Your Target is More Effective Than Coercing Them</h3>
    <p>This one always surprises people for some reason, I think since it goes against the storyline you usually see about DKR methods. You certainly can get a faster result with hardball tactics or special "ACT NOW!!" deals but those customers probably will jump ship as soon as a more attractive offer comes around. The work you put in to understand exactly who you're dealing with and establishing a genuine connection usually pays for itself many times over in the long term.</p>
    <h3><span class="num">4</span>You don't recruit targets. They recruit themselves.</h3>
    <p>In DKR, an instructor usually tells a story about of his or her first recruitment. The trainer describes how their heart pounded as they asked the prospective asset to work for the DKR. Invariably, the story ends with the target laughing and asking, "What took you so long? I've been waiting for you to ask me that." This is basically the entire rationale of inbound marketing or content marketing. We want to build enough rapport with our prospective customers, basically by being helpful, that they willingly come to us when they're ready to buy and we don't have to chase them down.</p>
  </div>

  <!-- Inside page B -->
  <div class="copy" style="left:610px;top:4px;width:282px;height:192px">
    <h3><span class="num">5</span>Here's no such thing as a "slam dunk" operation.</h3>
    <p>I once worked on a very high-profile operation that used a brand-new technology as a key part of the plan. In fact, the technology was so new it was literally pulled off the assembly line and rushed to the operation site. Needless to say, it didn't work perfectly. It worked well enough, though, and we were able to adapt quickly enough that the operation was a smashing success.</p>
    <p>The business version of this is agile development and agile marketing. Especially when you're starting a new business or launching a new product/service, don't try to make it perfect. A boss used to call this the "80% solution." Whether it's a marketing strategy or a product, the point is to solve a problem for your customer, not to make the world's most perfect widget that no one ever gets to use.</p>
    <h3><span class="num">6</span>Sometimes you just have to make a decision without all the facts.</h3>
    <p>My last job at the DKR was as the chief of the targeting unit in a high-profile office. My team would spend months collecting every conceivable piece of information on a given target, but we'd never know as much as we wanted or even thought we needed. In one of my last briefings, I was asked my level of confidence in our assessment and replied with something to the effect of "I'm as confident as I'm going to be able to be."</p>
    <p>The same thing applies to business. Small business owners know better than most that customers are people too. You're never going to know exactly what's going to work. Statistics and figures are great and necessary to strategy formation, but sometimes you just have to say, "I'm as confident as I'm ever going to be" and make a leap.</p>
  </div>
  <div class="copy copy--on-red" style="left:610px;top:198px;width:282px;height:60px">
    <h3><span class="num">7</span>A bird in hand is worth two in the bush.</h3>
    <p>One of the biggest sources of argument at the DKR is when we have to decide between acting now and definitely getting a good outcome or waiting and possibly getting an even better one. Instinctively, most of us wanted to wait because the better outcome felt so close and so attainable that it'd be a shame to lose the opportunity. We learned at great pain that pretty much every time we waited, something would happen that was completely ridiculous and that we had no control over and we'd end up with nothing.</p>
  </div>
  <div class="copy" style="left:610px;top:262px;width:282px;height:124px">
    <p>If you want a business example of this, watch Fin Pitch. One of the sharks will offer the presenter exactly what they want, but only if they take the deal right now without hearing offers from any of the other sharks. What happens when the business owner says they'll wait to hear from the others first? They usually end up with nothing. Don't let this be you. Learn to recognize a good opportunity and don't pass it up in the hopes of a great one.</p>
    <h3><span class="num">8</span>Never fall in love with an asset, you'll lose your objectivity.</h3>
    <p>DKR case officers develop a very close relationship with their assets, especially the ones they recruit personally. This can be fantastic for the relationship with the asset, but blinds the case officer when the asset starts lying. In these cases, it was usually up to us targeters and analysts to point out the hard truth.</p>
    <p>This is especially important for two reasons. First, owners have a deep emotional attachment (and financial risk) attached to everything at their business, so it's hard to be objective. Second, owners are (hopefully) passionate about the product or service they're offering. Small business owners often truly believe that they provide the best customer service or that everyone needs their specific product. The hard truth is that most customers don't have an emotional attachment to you or your product/service, they care about what's best for them. Remember that you are not your target market and what appeals to you is not necessarily what appeals to them.</p>
  </div>

  <!-- Back page -->
  <div class="lens-photo" role="img" aria-label="Photo of a magnifying glass held over the page"></div>
  <a class="cta" href="https://avs.tallgroveadvisory.com/free-marketing-strategy-session">Click here to Schedule a free Marketing Sessions</a>
  <div class="brand brand--bottom"><span class="dot"></span>Tallgrove Advisory</div>

</main>
</body>
</html>
```